Steps to get a free fence estimate

Hi! I need a new flyer in the similar design / style that you created previously for us! I would like this one to showcase the steps to get a free estimate.
There are several options to obtain a free fence quote for your fence installation or to buy fence materials:
1) In-Person - In-person quotes are available for fence installations only. Call, email or message us online to schedule an in-person measurement at your property.
2) Virtual Quotes - Send us your lot survey, fence layout diagram with dimensions, or measure your property online using our Web Yard Sizing Helper. We can review the dimensions to provide a site-unseen quote. You can also call us with your project information for a quote via phone.
3) Competitor Quotes - Send us the quotes from qualified competitors for price comparisons. Competitor quotes must have fence style, footage, and other project information.
What information do we need to give you a free estimate?
Fence footage - how many feet of fencing do you need?
Fence style - what fence style and material would you like quoted?
Fence placement - does the fence need to be installed in concrete or asphalt surfaces? or will it be installed in normal dirt areas?
Gate information - do you need any single person walk through gates, or a larger double gate? (walk gates can be 3FT, 4FT and 5FT wide - 5FT wide is wide enough for a riding lawn mower to get through. double gates can be 8FT, 10FT and 12FT wide.)
For installation quotes, please let us know any additional information such as if there is any existing fencing to remove, obstacles in the path of the fence line or if the fence has to be installed on top of concrete/asphalt surfaces.
We make the fence quoting process easy and simple!
Lifetime warranty on workmanship, labor and manufacturer's lifetime warranty on materials.
---
This flyer only needs to discuss the steps to obtaining a free fence estimate for our customers.

```html
<!DOCTYPE html>
<html lang="en">
<head>
<meta charset="utf-8">
<title>Steps to Get a Free Fence Estimate</title>
<link href="https://fonts.googleapis.com/css2?family=Comic+Neue:wght@700&family=Lato:wght@400;700&display=swap" rel="stylesheet">
<style>
  :root {
    --backdrop: #e6e6e6;
    --brand-blue: #44a3cc;
    --label-blue: #3b9ccb;
    --panel-white: #f6f6f6;
    --ink: #141414;
    --arrow-fill: #ec7f8c;
    --arrow-edge: #3b8fc0;
    --qmark-edge: #1f4d63;
    --on-blue: #ffffff;
  }
  * { margin: 0; padding: 0; box-sizing: border-box; }
  html, body {
    width: 1200px; height: 1200px; overflow: hidden;
    background: var(--backdrop);
  }
  .flyer {
    position: absolute; left: 40px; top: 40px;
    width: 1120px; height: 1120px;
    background: var(--brand-blue);
    box-shadow: 0 2px 6px rgba(0,0,0,0.18);
    overflow: hidden;
  }
  .flyer-shape { position: absolute; inset: 0; width: 100%; height: 100%; }

  .headline, .section-title, .closing-line {
    position: absolute; left: 0; right: 0; text-align: center;
    font-family: "Comic Neue", "Comic Sans MS", cursive;
    font-weight: 700; color: var(--ink); letter-spacing: 0.5px;
  }
  .headline { top: 88px; font-size: 36px; }
  .intro {
    position: absolute; top: 145px; left: 70px; right: 60px;
    text-align: center;
    font-family: "Lato", Arial, sans-serif; font-size: 19px; color: var(--ink);
  }

  .quote-options {
    position: absolute; top: 192px; left: 70px; right: 60px;
    display: flex; gap: 34px;
  }
  .quote-option { flex: 1; }
  .option-label {
    font-family: "Comic Neue", "Comic Sans MS", cursive;
    font-weight: 700; font-size: 25px; line-height: 32px;
    color: var(--label-blue); margin-bottom: 6px;
  }
  .option-text {
    font-family: "Lato", Arial, sans-serif;
    font-size: 16px; line-height: 22px; color: var(--ink);
  }

  .section-title { top: 428px; font-size: 29px; }

  .info-row {
    position: absolute; left: 70px; right: 60px;
    display: flex; align-items: center;
    transform: translateY(-50%);
  }
  .info-label {
    width: 198px; flex: none;
    font-family: "Comic Neue", "Comic Sans MS", cursive;
    font-weight: 700; font-size: 27px; line-height: 34px;
    color: var(--label-blue);
  }
  .info-arrow { width: 52px; height: 18px; margin-right: 28px; flex: none; }
  .info-text {
    font-family: "Lato", Arial, sans-serif;
    font-size: 19px; line-height: 26px; color: var(--ink);
    max-width: 710px;
  }
  .qmark {
    font-family: "Comic Neue", "Comic Sans MS", cursive;
    font-weight: 700; font-size: 42px; line-height: 0;
    color: var(--label-blue);
    -webkit-text-stroke: 1.5px var(--qmark-edge);
    vertical-align: -5px; margin-left: 2px;
  }
  .row-footage { top: 505px; }
  .row-style { top: 585px; }
  .row-placement { top: 672px; }
  .row-gate { top: 775px; }

  .install-note {
    position: absolute; top: 838px; left: 70px; right: 60px;
    text-align: center;
    font-family: "Lato", Arial, sans-serif;
    font-size: 17px; line-height: 24px; color: var(--ink);
  }
  .closing-line { top: 910px; font-size: 26px; color: var(--label-blue); }

  .warranty {
    position: absolute; left: 0; right: 0; top: 1066px;
    text-align: center;
    font-family: "Lato", Arial, sans-serif;
    font-size: 21px; color: var(--on-blue);
  }
  .warranty strong { font-weight: 700; }
</style>
</head>
<body>
  <main class="flyer">
    <svg class="flyer-shape" viewBox="0 0 1120 1120" aria-hidden="true">
      <path fill="var(--panel-white)" d="M0,120 C15,75 80,62 190,60 L770,56 C860,54 905,20 985,20 C1060,20 1120,40 1120,58 L1120,985 C1060,972 990,988 900,1008 C780,1034 620,1022 450,1028 C280,1034 150,1026 70,1024 C30,1023 6,1030 0,1036 Z"/>
    </svg>

    <h1 class="headline">Steps to get a free fence estimate</h1>
    <p class="intro">There are several options to obtain a free fence quote for your fence installation or to buy fence materials:</p>

    <section class="quote-options">
      <div class="quote-option">
        <h2 class="option-label">1) In-Person</h2>
        <p class="option-text">In-person quotes are available for fence installations only. Call, email or message us online to schedule an in-person measurement at your property.</p>
      </div>
      <div class="quote-option">
        <h2 class="option-label">2) Virtual Quotes</h2>
        <p class="option-text">Send us your lot survey, fence layout diagram with dimensions, or measure your property online using our Web Yard Sizing Helper. We can review the dimensions to provide a site-unseen quote. You can also call us with your project information for a quote via phone.</p>
      </div>
      <div class="quote-option">
        <h2 class="option-label">3) Competitor Quotes</h2>
        <p class="option-text">Send us the quotes from qualified competitors for price comparisons. Competitor quotes must have fence style, footage, and other project information.</p>
      </div>
    </section>

    <h2 class="section-title">What information do we need to give you a free estimate?</h2>

    <section class="info-row row-footage">
      <div class="info-label">Fence<br>Footage</div>
      <svg class="info-arrow" viewBox="0 0 52 18" aria-hidden="true"><path d="M2,6 H36 V2 L50,9 L36,16 V12 H2 Z" fill="var(--arrow-fill)" stroke="var(--arrow-edge)" stroke-width="1.5" stroke-linejoin="round"/></svg>
      <p class="info-text">How many feet of fencing do you need<span class="qmark">?</span></p>
    </section>

    <section class="info-row row-style">
      <div class="info-label">Fence<br>Style</div>
      <svg class="info-arrow" viewBox="0 0 52 18" aria-hidden="true"><path d="M2,6 H36 V2 L50,9 L36,16 V12 H2 Z" fill="var(--arrow-fill)" stroke="var(--arrow-edge)" stroke-width="1.5" stroke-linejoin="round"/></svg>
      <p class="info-text">What fence style and material would you like quoted<span class="qmark">?</span></p>
    </section>

    <section class="info-row row-placement">
      <div class="info-label">Fence<br>Placement</div>
      <svg class="info-arrow" viewBox="0 0 52 18" aria-hidden="true"><path d="M2,6 H36 V2 L50,9 L36,16 V12 H2 Z" fill="var(--arrow-fill)" stroke="var(--arrow-edge)" stroke-width="1.5" stroke-linejoin="round"/></svg>
      <p class="info-text">Does the fence need to be installed in concrete or<br>asphalt surfaces? or will it be installed in normal dirt areas<span class="qmark">?</span></p>
    </section>

    <section class="info-row row-gate">
      <div class="info-label">Gate<br>information</div>
      <svg class="info-arrow" viewBox="0 0 52 18" aria-hidden="true"><path d="M2,6 H36 V2 L50,9 L36,16 V12 H2 Z" fill="var(--arrow-fill)" stroke="var(--arrow-edge)" stroke-width="1.5" stroke-linejoin="round"/></svg>
      <p class="info-text">Do you need any single person walk through gates, or a larger double gate? (walk gates can be 3FT, 4FT and 5FT wide - 5FT wide is wide enough for a riding lawn mower to get through. double gates can be 8FT, 10FT and 12FT wide.)</p>
    </section>

    <p class="install-note">For installation quotes, please let us know any additional information such as if there is any existing fencing to remove, obstacles in the path of the fence line or if the fence has to be installed on top of concrete/asphalt surfaces.</p>

    <p class="closing-line">We make the fence quoting process easy and simple!</p>

    <p class="warranty"><strong>Lifetime warranty</strong> on workmanship, labor and manufacturer's lifetime warranty on materials.</p>
  </main>
</body>
</html>
```